Quorvin Rapid Pregancy Test Box and Sterile Pouch.

We are a company that manufactures rapid diagnostic tests for pregnancy, drugs of abuse, disease, etc. We would like a box and pouch design for our tests. Each box approx (10 1/4" x 4 3/4"x 2 1/2") should be able to hold 40 pouches and the pouches are 4 6/16" x 2 7/16". We have a design currently, but we are not happy with it. we would prefer a more simple and elegant design. We will be marketing this to mainly hospitals, clinics and distributors and not at-home consumers. The design should have our Quorvin Logo and something that says FDA approved and 99% accuracy.
Updates

Logo, current box design and  current pouch image has been uploaded. Current box design image is for fertility hormones, but project is still for RAPID PREGNANCY TEST.

Target Market(s)

Hospitals, Government agencies, doctors, clinics.

Industry/Entity Type

Marketing

Requirements
Must have
• Box: Size, Logo, FDA approval, must denote femininity.

Pouch design must fit in with box design.

design should be on the horizontal for stacking purposes at hospitals. (read long flat box and pouch)
Nice to have
• Colors to match the color scheme of our Quorvin logo.
Should not have
• exceed size dimensions as our production line is set up for these sizes.

```html
<!DOCTYPE html>
<html lang="en">
<head>
<meta charset="utf-8">
<title>Quorvin Rapid Pregnancy Test – Box Front</title>
<link rel="stylesheet" href="https://fonts.googleapis.com/css2?family=Russo+One&family=Exo+2:wght@600;700&display=swap">
<style>
  :root {
    --backdrop: #ababab;
    --panel: #ffffff;
    --title-pink: #ea5a72;
    --title-shadow: rgba(90, 90, 100, 0.55);
    --brand-blue: #2f5fa8;
    --tick-red: #d2283c;
    --claim-white: #ffffff;
    --claim-shadow: rgba(40, 40, 70, 0.7);
    --orb-deep: #4d5c9c;
    --orb-mid: #8a77a4;
    --orb-rose: #c98a9c;
    --orb-haze: #9fb0d6;
    --haze-fade: #d7c9dd;
    --accent-peach: #f6ad9c;
    --timer-navy: #2b3570;
  }
  html, body {
    margin: 0;
    width: 1200px;
    height: 982px;
    overflow: hidden;
    background: var(--backdrop);
  }
  .box-front {
    position: absolute;
    left: 151px;
    top: 222px;
    width: 913px;
    height: 470px;
    background: var(--panel);
    box-shadow: 4px 6px 8px rgba(0, 0, 0, 0.35);
    overflow: hidden;
  }
  .box-front__orbs {
    position: absolute;
    left: 0;
    top: 0;
    width: 913px;
    height: 470px;
  }
  .product-title {
    position: absolute;
    left: 0;
    width: 926px;
    top: 172px;
    margin: 0;
    text-align: center;
    font-family: "Russo One", sans-serif;
    font-weight: 400;
    font-size: 54px;
    line-height: 1.2;
    letter-spacing: 1px;
    color: var(--title-pink);
    transform: skewX(-12deg);
    text-shadow: 3px 4px 3px var(--title-shadow);
  }
  .brand {
    position: absolute;
    left: 48px;
    top: 371px;
    display: flex;
    align-items: center;
    gap: 24px;
  }
  .brand__dot {
    width: 50px;
    height: 50px;
    border-radius: 50%;
    background: var(--brand-blue);
  }
  .brand__name {
    font-family: "Exo 2", sans-serif;
    font-weight: 600;
    font-size: 58px;
    line-height: 1;
    color: var(--brand-blue);
  }
  .claims {
    position: absolute;
    left: 556px;
    top: 320px;
    margin: 0;
    padding: 0;
    list-style: none;
  }
  .claim {
    display: flex;
    align-items: center;
    gap: 12px;
    height: 44px;
    margin-bottom: 19px;
    font-family: "Exo 2", sans-serif;
    font-weight: 700;
    font-size: 30px;
    color: var(--claim-white);
    text-shadow: 2px 2px 2px var(--claim-shadow);
  }
  .claim__icon {
    width: 42px;
    height: 42px;
    flex: none;
  }
</style>
</head>
<body>
  <section class="box-front">
    <svg class="box-front__orbs" viewBox="0 0 913 470" aria-hidden="true">
      <defs>
        <linearGradient id="orbFill" x1="0" y1="0" x2="0.3" y2="1">
          <stop offset="0" stop-color="var(--orb-deep)"/>
          <stop offset="0.55" stop-color="var(--orb-mid)"/>
          <stop offset="1" stop-color="var(--orb-rose)"/>
        </linearGradient>
        <linearGradient id="hazeFill" x1="0" y1="0" x2="1" y2="1">
          <stop offset="0" stop-color="var(--orb-haze)" stop-opacity="0.9"/>
          <stop offset="1" stop-color="var(--haze-fade)" stop-opacity="0.6"/>
        </linearGradient>
      </defs>
      <circle cx="938" cy="-23" r="105" fill="var(--accent-peach)"/>
      <circle cx="718" cy="281" r="276" fill="url(#hazeFill)"/>
      <circle cx="770" cy="262" r="237" fill="url(#orbFill)"/>
    </svg>

    <h1 class="product-title">RAPID PREGNANCY TEST</h1>

    <div class="brand">
      <span class="brand__dot"></span>
      <span class="brand__name">Quorvin</span>
    </div>

    <ul class="claims">
      <li class="claim">
        <svg class="claim__icon" viewBox="0 0 44 44" aria-hidden="true">
          <path d="M4 22 L16 36 L40 6 L17 28 Z" fill="var(--tick-red)"/>
        </svg>
        99% Accuracy
      </li>
      <li class="claim">
        <svg class="claim__icon" viewBox="0 0 44 44" aria-hidden="true">
          <circle cx="22" cy="24" r="17" fill="#ffffff" stroke="var(--timer-navy)" stroke-width="4"/>
          <path d="M22 24 L22 7 A17 17 0 0 1 37 17 Z" fill="var(--tick-red)"/>
          <rect x="18" y="1" width="8" height="4" fill="var(--timer-navy)"/>
        </svg>
        Fast Result
      </li>
    </ul>
  </section>
</body>
</html>
```